Business card design reauest

2 sided. White on both sides

Martin Oakhurst

Riverbend, Eastmoor

Cell Phone / Whatsapp/ Wechat/Zalo
1-555-382-7194
Moakhurst@kvpartsline.vn
Www.kvpartsline.vn
Www.kvpartsline.com

Industry/Entity Type

Sofa and furniture and kitchen

Contact Information for Business Card

2 sided. White on both sides Martin Oakhurst Riverbend, Eastmoor Cell Phone / Whatsapp/ Wechat/Zalo 1-555-382-7194 Moakhurst@kvpartsline.vn Www.kvpartsline.vn Www.kvpartsline.com

```html
<!DOCTYPE html>
<html lang="en">
<head>
<meta charset="utf-8">
<title>KV Parts Line – Business Card</title>
<link href="https://fonts.googleapis.com/css2?family=Cinzel:wght@500&family=Poppins:wght@400&display=swap" rel="stylesheet">
<style>
  :root {
    --green: #0b9a4a;
    --ink: #231f20;
    --white: #ffffff;
    --stage: #d6cbbb;
  }
  * { margin: 0; padding: 0; box-sizing: border-box; }
  html, body {
    width: 1189px; height: 1200px; overflow: hidden;
    background: var(--stage);
  }
  .canvas { position: relative; width: 1189px; height: 1200px; }

  .card {
    position: absolute; left: 168px;
    width: 852px; height: 486px;
    background: var(--white);
    overflow: hidden;
    box-shadow: 0 6px 16px rgba(0,0,0,0.25);
  }
  .card--front { top: 111px; }
  .card--back { top: 640px; }

  .card__band { position: absolute; inset: 0; }

  .brand {
    position: absolute;
    font-family: "Cinzel", serif;
    font-weight: 500;
    color: var(--green);
    white-space: nowrap;
    letter-spacing: 1px;
    transform: translateX(-50%);
  }
  .brand--front { left: 220px; top: 166px; font-size: 38px; }
  .brand--back { left: 426px; top: 262px; font-size: 50px; }

  .holder {
    position: absolute; left: 500px; top: 224px;
    font-family: "Cinzel", serif; font-weight: 500;
    font-size: 26px; color: var(--white); letter-spacing: 0.5px;
    white-space: nowrap;
  }
  .holder__rule {
    position: absolute; left: 502px; top: 266px;
    width: 121px; height: 3px; background: var(--ink);
  }

  .contacts {
    position: absolute; left: 502px; top: 288px;
    list-style: none;
    font-family: "Poppins", sans-serif; font-size: 20px;
    color: var(--white);
  }
  .contacts__item {
    display: flex; align-items: center; gap: 8px;
    height: 31px; white-space: nowrap;
  }
  .contacts__icon {
    width: 22px; height: 22px; flex: none;
    background: var(--white); border-radius: 2px;
    display: flex; align-items: center; justify-content: center;
  }
  .contacts__icon svg { width: 14px; height: 14px; }
</style>
</head>
<body>
<main class="canvas">
  <section class="card card--front">
    <svg class="card__band" width="852" height="486" viewBox="0 0 852 486" aria-hidden="true">
      <polygon points="674,0 852,0 852,486 126,486" fill="var(--green)"/>
    </svg>

    <div class="brand brand--front">KV PARTS LINE</div>

    <h1 class="holder">MARTIN OAKHURST</h1>
    <div class="holder__rule"></div>

    <ul class="contacts">
      <li class="contacts__item">
        <span class="contacts__icon">
          <svg viewBox="0 0 14 14"><rect x="3.5" y="1" width="7" height="12" rx="1" fill="none" stroke="var(--green)" stroke-width="1.6"/><rect x="5.5" y="10" width="3" height="1.2" fill="var(--green)"/></svg>
        </span>1-555-382-7194
      </li>
      <li class="contacts__item"><span class="contacts__icon"></span>moakhurst@kvpartsline.vn</li>
      <li class="contacts__item"><span class="contacts__icon"></span>www.kvpartsline.vn</li>
      <li class="contacts__item"><span class="contacts__icon"></span>www.kvpartsline.com</li>
      <li class="contacts__item">
        <span class="contacts__icon">
          <svg viewBox="0 0 14 14"><path d="M7 13 C4 9 2.5 7 2.5 5 A4.5 4.5 0 0 1 11.5 5 C11.5 7 10 9 7 13 Z" fill="none" stroke="var(--green)" stroke-width="1.5"/><circle cx="7" cy="5" r="1.6" fill="var(--green)"/></svg>
        </span>Riverbend, Eastmoor
      </li>
    </ul>
  </section>

  <section class="card card--back">
    <div class="brand brand--back">KV PARTS LINE</div>
  </section>
</main>
</body>
</html>
```